Health Coaching Flyer for New Clients

I need a two-sided flyer (3.5" x 8.5" preferred or 5" x 7") to distribute to potential coaching clients. My business name is Talvery Health & Wellness Coaching. My business is focused on helping people with habit changes that contribute to their overall well-being. I would like the design colors to be gender neutral. I would like a small photo of myself near the "my name is Joan" statement. Please feel free to change the logo color to match the design.

Target Market(s)

Adults of all ages.

Font styles to use
Serif

Requirements
Must have
• Emphasize my opening question (found in health coaching brochure - attached).
• Small picture of myself near "my name is Joan" statement.
Should not have
• No light of pastel colors.

```html
<!DOCTYPE html>
<html lang="en">
<head>
<meta charset="utf-8">
<title>Talvery Health &amp; Wellness Coaching – Rack Card</title>
<link href="https://fonts.googleapis.com/css2?family=Poppins:wght@600;700;800&family=Raleway:ital,wght@0,500;1,500&family=Open+Sans:wght@400&display=swap" rel="stylesheet">
<style>
  :root {
    --backdrop: #cfcfcf;
    --paper: #f1f1f1;
    --indigo: #2a2a8a;
    --indigo-text: #2e2e93;
    --ink: #111111;
    --white: #ffffff;
    --photo-dark: #2c1f1a;
    --photo-warm: #8a5a44;
  }
  * { margin: 0; padding: 0; box-sizing: border-box; }
  html, body { width: 1200px; height: 1023px; overflow: hidden; }
  body { background: var(--backdrop); position: relative; font-family: "Raleway", sans-serif; }

  .card {
    position: absolute; top: 126px; width: 313px; height: 766px;
    background: var(--paper); overflow: hidden;
    box-shadow: 0 18px 30px rgba(0,0,0,0.18);
  }
  .card--front { left: 242px; }
  .card--back { left: 638px; }

  /* Front */
  .brand { position: absolute; left: 20px; top: 26px; color: var(--ink); font-family: "Poppins", sans-serif; font-weight: 700; }
  .brand__name { font-size: 47px; line-height: 44px; letter-spacing: 7px; }
  .brand__tag { font-size: 11.5px; line-height: 15px; letter-spacing: -0.2px; }

  .portrait {
    position: absolute; left: 0; top: 98px; width: 313px; height: 457px;
    background: radial-gradient(ellipse at 50% 35%, #b9876c 0%, var(--photo-warm) 30%, #4a2e24 65%, var(--photo-dark) 100%);
  }
  .headline { position: absolute; left: 24px; top: 386px; color: var(--white); font-family: "Poppins", sans-serif; }
  .headline__ask { font-size: 32px; font-weight: 700; line-height: 31px; letter-spacing: 5px; }
  .headline__sub { margin-top: 16px; font-size: 16.5px; font-weight: 600; line-height: 19.6px; letter-spacing: 3.3px; }
  .dots { display: flex; gap: 6px; }
  .dots span { width: 9px; height: 9px; border-radius: 50%; }
  .dots--light { position: absolute; left: 259px; top: 524px; }
  .dots--light span { background: var(--white); }

  .intro { position: absolute; left: 0; top: 555px; width: 313px; height: 211px; background: var(--indigo); color: var(--white); padding: 20px 40px 0 26px; }
  .intro__title { font-family: "Poppins", sans-serif; font-weight: 800; font-size: 26px; line-height: 30px; letter-spacing: 1.4px; white-space: nowrap; }
  .intro__text { margin-top: 10px; font-style: italic; font-size: 12.6px; line-height: 15.2px; }

  /* Back */
  .benefits__title { position: absolute; left: 30px; top: 38px; color: var(--indigo-text); font-family: "Poppins", sans-serif; font-weight: 700; font-size: 29px; line-height: 30px; }
  .benefit { position: absolute; left: 30px; width: 270px; display: flex; font-family: "Open Sans", sans-serif; font-size: 10.4px; line-height: 13.6px; color: var(--ink); }
  .benefit__num { width: 28px; flex: none; font-family: "Poppins", sans-serif; font-weight: 700; font-size: 25px; line-height: 24px; }
  .benefit__text { padding-top: 1px; }

  .invite { position: absolute; left: 0; top: 378px; width: 313px; height: 166px; background: var(--indigo); color: var(--white); padding: 22px 18px 0 25px; font-style: italic; font-size: 12.6px; line-height: 15.2px; }
  .invite p + p { margin-top: 17px; }

  .contact { position: absolute; left: 30px; top: 570px; color: var(--ink); }
  .contact__title { font-family: "Poppins", sans-serif; font-weight: 700; font-size: 24px; line-height: 28px; }
  .contact__note { font-size: 13.5px; line-height: 15.4px; font-weight: 500; }
  .dots--dark { margin-top: 17px; }
  .dots--dark span { background: var(--indigo-text); width: 8.5px; height: 8.5px; }
  .contact__name { margin-top: 12px; font-family: "Poppins", sans-serif; font-weight: 700; font-size: 24px; line-height: 28px; }
  .contact__line { font-size: 17px; line-height: 20px; letter-spacing: 1.6px; font-weight: 500; }
</style>
</head>
<body>
  <section class="card card--front">
    <div class="brand">
      <div class="brand__name">TALVERY</div>
      <div class="brand__tag">HEALTH &amp; WELLNESS COACHING</div>
    </div>
    <div class="portrait" role="img" aria-label="Portrait photo of Joan, the health coach, smiling"></div>
    <div class="headline">
      <div class="headline__ask">NEED<br>SUPPORT?</div>
      <div class="headline__sub">IN MAKING REAL,<br>LASTING LIFESTYLE<br>AND BEHAVIOR<br>CHANGES?</div>
    </div>
    <div class="dots dots--light"><span></span><span></span><span></span></div>
    <div class="intro">
      <h2 class="intro__title">My Name Is Joan</h2>
      <p class="intro__text">I am studying to become a THRIVE-Certified Functional Health Coach. My training involves many science-based practices that improve both our health and how we grow and change as humans. I now have the opportunity to turn that knowledge into practice by coaching actual clients interested in improving their own health and well-being.</p>
    </div>
  </section>

  <section class="card card--back">
    <h2 class="benefits__title">Functional<br>Health Coaches...</h2>
    <div class="benefit" style="top:128px"><span class="benefit__num">1</span><span class="benefit__text">Leverage your strengths rather than focus on your weaknesses.</span></div>
    <div class="benefit" style="top:170px"><span class="benefit__num">2</span><span class="benefit__text">Support you in finding your own strategies and motivation for change.</span></div>
    <div class="benefit" style="top:214px"><span class="benefit__num">3</span><span class="benefit__text">Provide a judgment-free zone and support your autonomy.</span></div>
    <div class="benefit" style="top:259px"><span class="benefit__num">4</span><span class="benefit__text">Use an experimental mindset to find and develop sustainable habits.</span></div>
    <div class="benefit" style="top:302px"><span class="benefit__num">5</span><span class="benefit__text">Act as your accountability partner as you reach your unique health goals;whether they be improving sleep, diet, fitness, social connection, or reducing stress.</span></div>

    <div class="invite">
      <p>I would like to invite you to participate with me as a client as I continue to hone my coaching skills. &nbsp;We can develop a plan and schedule that aligns with your goals.</p>
      <p>As a way to give back to my community, I am offering new clients six free coaching sessions. This is a limited time offer.</p>
    </div>

    <div class="contact">
      <h2 class="contact__title">Please Contact Me.</h2>
      <p class="contact__note">I’m ready to support you as you work<br>to improve your health.</p>
      <div class="dots dots--dark"><span></span><span></span><span></span></div>
      <div class="contact__name">Joan Talvery</div>
      <div class="contact__line">520-555-0147</div>
      <div class="contact__line">talveryhwc@mailbox.net</div>
    </div>
  </section>
</body>
</html>
```